Business Card Design Project

Business card, that is serious, yet elegant/upscale
Using both sides though only one for information
A space for a QR code would be good
basic contact details.
I will upload company logo
Updates

Thanks everyone who has submitted so far.  No additional designs are needed at this time, We could easily select from one of the many that are currebtly shown.

If you have a design in already and it is still listed it is in the running. Do not submit anymore, choosing now is hard enough given the talent and creativity shared.  WE are making a chpice today this evening.

Again thank you all.

Target Market(s)

CIo's, VP's and people at large companies

Industry/Entity Type

Business

Requirements
Must have
• The business card needs the basic ingo like:
The transparent gear/log enlarged on the card has been well received so is now a must forthe wining design

Name
Title

418 W. Dunmore
#2730
Chicago,Il 60817
Tel #

contact@merivane-example.com
Nice to have
• A QR Code, no glaring, but usable.

Should not have
• no cursive/handwriting fonts.

```html
<!DOCTYPE html>
<html lang="en">
<head>
<meta charset="utf-8">
<title>Merivane Group — Business Card</title>
<link rel="stylesheet" href="https://fonts.googleapis.com/css2?family=Cutive+Mono&family=Source+Sans+3:wght@400;600&display=swap">
<style>
  :root {
    --page-bg: #ffffff;
    --card-bg: #ffffff;
    --brand-green: #1a9a50;
    --ink-grey: #58585a;
    --label-grey: #555557;
    --side-label: #444444;
    --qr-line: #b9b9bb;
    --card-shadow: rgba(0, 0, 0, 0.28);
  }
  * { box-sizing: border-box; margin: 0; padding: 0; }
  html, body {
    width: 1200px;
    height: 979px;
    overflow: hidden;
    background: var(--page-bg);
  }
  .sheet {
    position: relative;
    width: 1200px;
    height: 979px;
    font-family: "Source Sans 3", "Myriad Pro", Arial, sans-serif;
  }
  .side-label {
    position: absolute;
    font-family: "Cutive Mono", "Courier New", monospace;
    font-size: 22px;
    color: var(--side-label);
    letter-spacing: 0.5px;
  }
  .side-label--front { left: 209px; top: 120px; }
  .side-label--back  { left: 205px; top: 544px; }

  .card {
    position: absolute;
    width: 506px;
    height: 318px;
    background: var(--card-bg);
    box-shadow: 0 3px 6px var(--card-shadow);
  }
  .card--front { left: 441px; top: 116px; }
  .card--back  { left: 443px; top: 540px; }

  /* Front: name lockup */
  .brand-mark {
    position: absolute;
    left: 64px;
    top: 106px;
    width: 86px;
    height: 86px;
    border-radius: 50%;
    background: var(--brand-green);
  }
  .brand-name {
    position: absolute;
    left: 164px;
    top: 120px;
    font-size: 44px;
    font-weight: 600;
    color: var(--brand-green);
    letter-spacing: -1px;
    line-height: 1;
    white-space: nowrap;
  }
  .brand-tagline {
    position: absolute;
    right: 60px;
    top: 177px;
    font-size: 14px;
    color: var(--brand-green);
    letter-spacing: 3.3px;
    line-height: 1;
    white-space: nowrap;
  }

  /* Back: contact details */
  .company-name {
    position: absolute;
    left: 61px;
    top: 36px;
    font-size: 31px;
    font-weight: 600;
    color: var(--ink-grey);
    letter-spacing: -0.6px;
    line-height: 1;
  }
  .person {
    position: absolute;
    left: 62px;
    top: 72px;
    line-height: 1;
  }
  .person-name {
    display: block;
    font-size: 16px;
    font-weight: 600;
    color: var(--ink-grey);
  }
  .person-title {
    display: block;
    margin-top: 3px;
    font-size: 13px;
    color: var(--ink-grey);
    letter-spacing: 0.3px;
  }
  .contact-block {
    position: absolute;
    left: 61px;
  }
  .contact-block--address { top: 111px; }
  .contact-block--call    { top: 171px; }
  .contact-block--email   { top: 231px; }
  .contact-label {
    display: inline-block;
    background: var(--label-grey);
    color: #ffffff;
    font-size: 13px;
    font-weight: 600;
    line-height: 18px;
    padding: 0 4px;
    letter-spacing: 0.4px;
  }
  .contact-value {
    display: block;
    margin-top: 3px;
    font-size: 21px;
    color: var(--brand-green);
    line-height: 26px;
    white-space: nowrap;
  }
  .contact-value .gap { display: inline-block; width: 18px; }

  .qr-space {
    position: absolute;
    right: 40px;
    bottom: 38px;
    width: 78px;
    height: 78px;
    border: 1px solid var(--qr-line);
  }
</style>
</head>
<body>
  <main class="sheet">
    <span class="side-label side-label--front">front</span>
    <section class="card card--front" aria-label="Card front">
      <span class="brand-mark" aria-hidden="true"></span>
      <span class="brand-name">Merivane Group</span>
      <span class="brand-tagline">software + service</span>
    </section>

    <span class="side-label side-label--back">back</span>
    <section class="card card--back" aria-label="Card back">
      <h1 class="company-name">Merivane Group</h1>
      <p class="person">
        <span class="person-name">Name</span>
        <span class="person-title">Title</span>
      </p>
      <div class="contact-block contact-block--address">
        <span class="contact-label">Address</span>
        <span class="contact-value">418 W. Dunmore<span class="gap"></span>#2730<span class="gap"></span>Chicago, Il 60817</span>
      </div>
      <div class="contact-block contact-block--call">
        <span class="contact-label">Call</span>
        <span class="contact-value">Tel #</span>
      </div>
      <div class="contact-block contact-block--email">
        <span class="contact-label">Email</span>
        <span class="contact-value">contact@merivane-example.com</span>
      </div>
      <div class="qr-space" role="img" aria-label="Space reserved for QR code"></div>
    </section>
  </main>
</body>
</html>
```